Scholarly Steering Board for Wayfinding Inquiry and Learning

This flyer will be the initial identifying document to launch the brand awareness for this new non-profit. So it needs to be both informational and dynamic in visual appeal since our organization focuses on visual communications. It must also be designed to be sent electronically. Perhaps a two sided one page design would work best but open to suggestions.

Target Market(s)

Academia, marketing/advertising professionals, sign industry, small businesses.

Industry/Entity Type

Education

Requirements
Must have
• High visual appeal with fundamental narrative; logo as submitted. Response sensitive and ease in electronically delivery format. Website identified as well as Twitter and Facebook. Website is www.ssbwil.org. Use colors and font that go with logo.
Nice to have
• Focus on scope of work especially emphasis on collaboration and innovation; thought leadership.
Should not have
• Cookie cutter look. Anything that could be not used to build complimentary collateral literature.

```html
<!DOCTYPE html>
<html lang="en">
<head>
<meta charset="utf-8">
<title>SSBWIL Flyer</title>
<link href="https://fonts.googleapis.com/css2?family=Raleway:wght@400;500;600;700&display=swap" rel="stylesheet">
<style>
  :root{
    --stage:#e9eaec;
    --navy:#0d2f57;
    --blue:#175d8f;
    --blue-light:#2a7bb0;
    --paper:#ffffff;
    --paper-shade:#e6e6e8;
    --ink:#2b2b2b;
    --frame:#ffffff;
  }
  *{box-sizing:border-box;margin:0;padding:0}
  html,body{width:1200px;height:960px;overflow:hidden}
  body{background:var(--stage);font-family:"Raleway",sans-serif;position:relative}
  .flyer{position:absolute;left:246px;top:22px;width:708px;height:917px;overflow:hidden;background:var(--paper);box-shadow:0 2px 10px rgba(0,0,0,.15)}
  .hero-photo{position:absolute;left:0;top:0;width:708px;height:520px;
    background:linear-gradient(180deg,#b07a5e 0%,#c9a48a 25%,#d9c6b4 45%,#8a7468 70%,#6c5a52 100%)}
  .shapes{position:absolute;left:0;top:0}
  .snapshot{position:absolute;width:161px;height:140px;border:3px solid var(--frame);border-radius:10px;overflow:hidden}
  .snapshot-meeting{left:48px;top:290px;background:linear-gradient(160deg,#8c7764,#c9b8a5 55%,#3b3540)}
  .snapshot-tour{left:205px;top:320px;background:linear-gradient(160deg,#c8c9cc,#9ba0a8 50%,#4d4b50)}
  .snapshot-session{left:363px;top:353px;background:linear-gradient(160deg,#bcae9c,#8a8f98 55%,#2f3646)}
  .brand{position:absolute;left:55px;top:508px;display:flex;align-items:center;gap:6px}
  .brand-square{width:14px;height:14px;background:var(--paper)}
  .brand-name{font-weight:700;font-size:24px;color:var(--paper);letter-spacing:.5px}
  .intro{position:absolute;left:13px;top:568px;width:284px;color:var(--paper)}
  .kicker{font-size:16px;font-weight:600;line-height:20px;color:#d6e6f3;margin-bottom:10px}
  .headline{font-size:24px;font-weight:600;line-height:1.2;margin-bottom:14px}
  .intro p{font-size:11.6px;line-height:14.5px;margin-bottom:13px}
  .intro p:last-child{margin-bottom:0}
  .intro a{color:var(--paper);font-weight:700;text-decoration:underline}
  .scope{position:absolute;left:335px;top:506px;width:362px;color:var(--ink)}
  .scope ul{list-style:none}
  .scope li{position:relative;padding-left:10px;font-size:10.3px;line-height:1.22;margin-bottom:8px}
  .scope li::before{content:"•";position:absolute;left:0;top:0}
  .scope .closing{font-size:10.3px;line-height:1.22;text-align:justify;margin-top:2px}
</style>
</head>
<body>
<main class="flyer">
  <div class="hero-photo" role="img" aria-label="Photo of a diverse team gathered around a table in a brick-walled office, discussing ideas"></div>
  <svg class="shapes" width="708" height="917" viewBox="0 0 708 917" aria-hidden="true">
    <defs>
      <linearGradient id="blueFill" x1="0" y1="0" x2="0" y2="1">
        <stop offset="0" stop-color="var(--blue-light)"/>
        <stop offset=".5" stop-color="var(--blue)"/>
        <stop offset="1" stop-color="var(--navy)"/>
      </linearGradient>
      <linearGradient id="paperFill" x1="0" y1="0" x2="0" y2="1">
        <stop offset="0" stop-color="var(--paper)"/>
        <stop offset="1" stop-color="var(--paper-shade)"/>
      </linearGradient>
    </defs>
    <path d="M0,355 C90,330 200,380 262,445 C335,525 335,700 298,917 L0,917 Z" fill="url(#blueFill)"/>
    <path d="M298,917 C335,700 335,560 318,480 C450,505 580,490 708,470 L708,917 Z" fill="url(#paperFill)"/>
  </svg>
  <div class="snapshot snapshot-meeting" role="img" aria-label="Photo of council members meeting around a table"></div>
  <div class="snapshot snapshot-tour" role="img" aria-label="Photo of a guided tour through a sign fabrication facility"></div>
  <div class="snapshot snapshot-session" role="img" aria-label="Photo of a working session with laptops in a conference room"></div>

  <div class="brand">
    <span class="brand-square"></span>
    <span class="brand-name">SSBWIL</span>
  </div>

  <section class="intro">
    <h2 class="kicker">Innovation at the Crossroads:</h2>
    <h1 class="headline">Building Thought Leadership for Signage Research and Education</h1>
    <p>Please consider joining the movement as the Scholarly Steering Board for Wayfinding Inquiry and Learning (SSBWIL) labors to provide <a href="#">independent thought leadership</a> in an exciting interdisciplinary space.</p>
    <p>Our intent is to <a href="#">advance the study of the science, technology, art/advertising and regulation of on-premise signage.</a> Faculty from thirteen universities along with thought leaders from the sign industry are driving the SSBWIL initiatives.</p>
    <p>Perhaps you will <a href="#">support</a> one or more of the following areas where SSBWIL is making an impact:</p>
  </section>

  <section class="scope">
    <ul>
      <li>Identifying research, educational needs and opportunities within academia and professional settings commensurate with prioritizing research and education initiatives that embrace emerging topics/trends for signage applicability.</li>
      <li>Generating benchmarking exercises.</li>
      <li>Measuring the impact of generated work products.</li>
      <li>Providing assessment and guidance to current and future peer-review processes.</li>
      <li>Identifying new funding opportunities.</li>
      <li>Identifying a comprehensive network of subject-matter experts.</li>
      <li>Identifying a multi-disciplinary component within each university and implementing immersion and integration efforts that build and advance innovative strategies from each member university.</li>
      <li>Expanding SSBWIL involvement to additional universities.</li>
      <li>Identifying and aligning with professional associations and related organizations.</li>
      <li>Participating in the peer-review research process to provide assessment and guidance to current and future peer-reviewed processes.</li>
      <li>Providing technical expertise on how signage is addressed within each academic discipline to create cross-disciplinary dialogue on signage research needs.</li>
    </ul>
    <p class="closing">After receiving a generous challenge donation from a donor, SSBWIL is sharing its work scope to cultivate a broad base of donors. Please consider contributing to SSBWIL's efforts to maximize the impact and reach of this challenge donation.</p>
  </section>
</main>
</body>
</html>
```